Business Card Update, need to bring life to the card, two sided color

We need a new business card design, are moving and changing addresses and need a new look, we have the logos already attached but need a new style moving forward. Can incorporate the color of the logo (The Green) as well, maybe a solid back? We deal with safety products revolving around static electricity and safety lighting. Would like to keep same font in second logo as well.

Target Market(s)

Electrical Safety, Lighting

Contact Information for Business Card

Lars Whitcombe
Vice President
Office: 555-284-7316
Cell: 555-862-0457
lars@tkwhitcombe.com
www.tkwhitcombe.com
4700 West Cedar Boulevard
Suite #320
Roswell, GA 30412

Font styles to use
Serif
Sans Serif

Requirements
Must have
• Since 1918
Nice to have
• Could use the 100 Year Logo for back of card, would like the back of card to be the same green as logo.
Should not have
• No black cards please.

```html
<!DOCTYPE html>
<html lang="en">
<head>
<meta charset="utf-8">
<title>T.K. Whitcombe Business Card</title>
<link rel="stylesheet" href="https://fonts.googleapis.com/css2?family=Lato:wght@400;700&family=Arimo:wght@700&display=swap">
<style>
  :root {
    --brand-green: #03995a;
    --paper-white: #ffffff;
    --backdrop: #e6e7e8;
    --card-shadow: rgba(0, 0, 0, 0.35);
  }
  * { margin: 0; padding: 0; box-sizing: border-box; }
  html, body {
    width: 1200px; height: 802px; overflow: hidden;
    background: var(--backdrop);
  }
  .stage { position: relative; width: 1200px; height: 802px; }
  .card {
    position: absolute; top: 274px;
    width: 443px; height: 265px;
    background: var(--brand-green);
    overflow: hidden;
    box-shadow: 2px 3px 6px var(--card-shadow);
    color: var(--paper-white);
  }
  .card--front { left: 136px; }
  .card--back { left: 624px; }

  /* Front: brand seal area */
  .brand-seal {
    position: absolute; left: -12px; top: 14px;
    width: 236px; height: 236px; border-radius: 50%;
    background: var(--paper-white);
    display: flex; flex-direction: column; align-items: center; justify-content: center;
    text-align: center; color: var(--brand-green);
    font-family: "Lato", sans-serif; font-weight: 700;
  }
  .brand-seal__name { font-size: 24px; line-height: 1.15; letter-spacing: 1px; }
  .brand-seal__since { margin-top: 8px; font-size: 11px; letter-spacing: 2px; }

  /* Front: contact block */
  .contact {
    position: absolute; right: 22px; top: 55px;
    text-align: right;
    font-family: "Lato", sans-serif;
  }
  .contact__name { font-weight: 700; font-size: 16px; letter-spacing: 0.2px; line-height: 18px; }
  .contact__title { font-size: 13px; line-height: 16px; }
  .contact__list { list-style: none; margin-top: 12px; }
  .contact__list li {
    font-size: 12.5px; line-height: 16px;
    display: flex; justify-content: flex-end; align-items: center; gap: 2px;
  }
  .contact__list svg { width: 10px; height: 10px; fill: var(--paper-white); }
  .contact__address { margin-top: 12px; font-size: 12.5px; line-height: 16px; font-style: normal; }

  /* Back: centered brand lockup */
  .lockup {
    position: absolute; left: 79px; top: 97px;
    display: flex; align-items: center; gap: 9px;
  }
  .lockup__mark {
    width: 70px; height: 70px; border-radius: 50%;
    border: 3px solid var(--paper-white);
  }
  .lockup__text { font-family: "Arimo", sans-serif; font-weight: 700; }
  .lockup__name { font-size: 23px; line-height: 25px; }
  .lockup__sub { font-size: 11.5px; line-height: 14px; padding-left: 14px; letter-spacing: 0.3px; }
</style>
</head>
<body>
<main class="stage">
  <section class="card card--front">
    <div class="brand-seal">
      <span class="brand-seal__name">T.K.<br>WHITCOMBE</span>
      <span class="brand-seal__since">SINCE 1918</span>
    </div>
    <div class="contact">
      <p class="contact__name">LARS WHITCOMBE</p>
      <p class="contact__title">Vice President</p>
      <ul class="contact__list">
        <li>555-284-7316<svg viewBox="0 0 10 10"><path d="M1 4c0-2 1-3 4-3s4 1 4 3H7V3H3v1zM2 5h6l1 4H1z"/></svg></li>
        <li>555-862-0457<svg viewBox="0 0 10 10"><path d="M3 0h4a1 1 0 0 1 1 1v8a1 1 0 0 1-1 1H3a1 1 0 0 1-1-1V1a1 1 0 0 1 1-1zm0 1.5v6h4v-6z"/></svg></li>
        <li>lars@tkwhitcombe.com<svg viewBox="0 0 10 10"><path d="M0 2h10v6H0zM1 3l4 3 4-3v-.2H1z"/></svg></li>
        <li>www.tkwhitcombe.com<svg viewBox="0 0 10 10"><circle cx="5" cy="5" r="4.5"/></svg></li>
      </ul>
      <address class="contact__address">4700 West Cedar Boulevard<br>Suite #320, Roswell, GA 30412</address>
    </div>
  </section>

  <section class="card card--back">
    <div class="lockup">
      <div class="lockup__mark"></div>
      <div class="lockup__text">
        <p class="lockup__name">T.K. Whitcombe</p>
        <p class="lockup__sub">Manufacturing Company, Inc.</p>
      </div>
    </div>
  </section>
</main>
</body>
</html>
```